new letterhead/envelope/business card design for law firm

please see attached pdf of current letterhead, envelope and business card. I am also attaching my new logo that I would like to be used. basically, I am looking to refresh and simplify my letterhead/stationary and business card, keeping the following in mind:

overall, I am going for the following look:

-simple,
-modern,
-classy,
-professional

Target Market(s)

law firm clients

Industry/Entity Type

Law Firm

Contact Information for Business Card

see attachment

Font styles to use
Sans Serif

Requirements
Must have
• overall, I am going for the following look:
• -simple,
• -modern,
• -classy,
• -professional
Nice to have
• same as above
Should not have
• no serif fonts

```html
<!DOCTYPE html>
<html lang="en">
<head>
<meta charset="utf-8">
<title>Halden Law Stationery</title>
<link rel="stylesheet" href="https://fonts.googleapis.com/css2?family=Roboto:wght@400;700&family=Didact+Gothic&display=swap">
<style>
:root{
  --bg:#dcdcdc;
  --paper:#f7f7f7;
  --navy:#0e2a4e;
  --green:#2f6b3f;
  --ink:#4a4a4a;
  --muted:#666;
  --sig:#2a5bb0;
}
*{margin:0;padding:0;box-sizing:border-box}
html,body{width:1200px;height:877px;overflow:hidden;background:var(--bg)}
body{position:relative;font-family:"Roboto",sans-serif;color:var(--ink)}
.sheet{position:absolute;background:linear-gradient(120deg,#fbfbfb,#f0f0f0);box-shadow:0 1px 4px rgba(0,0,0,.25)}
.brand{position:absolute;text-align:center;transform:translateX(-50%)}
.brand-mark{display:block;margin:0 auto;border-radius:50%;background:var(--navy)}
.brand-name{display:block;font-family:"Roboto",sans-serif;font-weight:700;color:var(--navy);letter-spacing:.12em;white-space:nowrap}

/* letterhead */
.letterhead{left:58px;top:64px;width:528px;height:742px}
.letterhead .brand{left:264px;top:40px}
.letterhead .brand-mark{width:44px;height:44px;margin-bottom:8px}
.letterhead .brand-name{font-size:21px}
.salutation{position:absolute;left:45px;top:208px;font-family:"Didact Gothic",sans-serif;font-size:13px;color:#555}
.letter-body{position:absolute;left:45px;top:247px;width:439px;font-family:"Didact Gothic",sans-serif;font-size:7.4px;line-height:11.3px;color:#555;text-align:justify}
.letter-body p{margin-bottom:11.5px}
.closing{position:absolute;left:45px;top:486px;font-family:"Didact Gothic",sans-serif;font-size:7.6px;color:#555}
.signature{position:absolute;left:42px;top:520px;width:94px;height:38px;background:linear-gradient(90deg,rgba(42,91,176,.18),rgba(42,91,176,.06));border-radius:4px}
.lh-footer-left{position:absolute;left:45px;top:662px;font-size:7.6px;line-height:9.6px;color:var(--muted)}
.lh-footer-left strong{display:block;font-size:9.6px;color:var(--navy);margin-bottom:2px}
.lh-footer-right{position:absolute;right:44px;top:662px;text-align:right;font-size:7.6px;line-height:10.4px;color:var(--muted)}
.lh-footer-right b{color:var(--navy)}
.gap{display:block;height:3px}

/* cards */
.card-front{left:606px;top:88px;width:252px;height:144px}
.card-front .brand{left:62px;top:44px}
.card-front .brand-mark{width:32px;height:32px;margin-bottom:6px}
.card-front .brand-name{font-size:15px}
.card-contact{position:absolute;right:19px;top:22px;text-align:right;font-size:5.8px;line-height:8px;color:var(--muted)}
.card-contact .name{font-size:8.4px;font-weight:700;color:var(--navy);line-height:10px}
.card-contact .lic{color:var(--green);margin-bottom:20px}
.card-contact b{color:var(--navy)}
.card-back{left:878px;top:88px;width:252px;height:144px}
.card-back .brand-mark{position:absolute;left:86px;top:27px;width:80px;height:80px}
.card-back .site{position:absolute;left:0;right:0;top:124px;text-align:center;font-size:5.8px;letter-spacing:.35em;color:var(--muted)}

/* envelopes */
.envelope-back{left:603px;top:269px;width:531px;height:240px;background:linear-gradient(180deg,#f3f3f3,#e9e9e9)}
.flap{position:absolute;left:0;top:0;width:531px;height:76px}
.envelope-back .brand-mark{position:absolute;left:248px;top:20px;width:35px;height:35px}
.envelope-front{left:603px;top:562px;width:533px;height:242px}
.envelope-front .brand{left:83px;top:34px}
.envelope-front .brand-mark{width:37px;height:37px;margin-bottom:7px}
.envelope-front .brand-name{font-size:17px}
.envelope-front .address{margin-top:8px;font-size:7.6px;line-height:9.6px;color:var(--navy)}
</style>
</head>
<body>

<section class="sheet letterhead">
  <div class="brand">
    <span class="brand-mark"></span>
    <span class="brand-name">HALDEN LAW</span>
  </div>
  <p class="salutation">Dear Mr. Ellison,</p>
  <div class="letter-body">
    <p>Lorem ipsum dolor sit amet, consectetur adipiscing elit. Donec orci purus, luctus vitae dignissim eu, iaculis sed purus. Vivamus faucibus, ipsum nec aliquet viverra, leo mauris condimentum ligula, sit amet sagittis enim ligula quis arcu. Nam egestas tortor id nisi porttitor mattis. In tortor ante, ultricies in suscipit a, tempus non massa. Vivamus et auctor mi. Fusce vel massa nulla. Phasellus nec eros mauris, et scelerisque orci.</p>
    <p>Donec malesuada orci vitae nulla accumsan porta a id massa. Quisque accumsan iaculis magna sit amet fringilla. Maecenas consequat, magna eget tincidunt semper, odio nibh rutrum mi, id feugiat ante nisi eu risus. Vestibulum nunc orci, rhoncus a placerat in, ultricies in mi. Cras mattis varius eros, vel fringilla nisi suscipit eget. Quisque scelerisque sagittis nulla at porttitor.</p>
    <p>Sed id augue vitae urna euismod commodo aliquet a quam. Pellentesque arcu velit, cursus et malesuada ut, consequat et diam. Nullam erat sem, rhoncus id ullamcorper vitae, rhoncus et arcu. In ultricies ultricies nulla, ut rutrum nisi iaculis at. Donec eu magna a metus ornare faucibus. Fusce aliquet faucibus ultricies. Morbi semper, est id tincidunt gravida, sem arcu adipiscing lacus, ac bibendum nulla leo eu purus. Quisque nec diam sed risus consectetur a ccumsan quis quis nibh. Vestibulum id purus lorem.</p>
    <p>It is a long established fact that a reader will be distracted by the readable content of a page when looking at its layout. The point of using Lorem Ipsum is that it has a more-or-less normal distribution of letters, as opposed to using 'Content here, content here', making it look like readable English. Many desktop publishing packages</p>
  </div>
  <p class="closing">Sincerely,</p>
  <div class="signature" role="img" aria-label="Handwritten signature"></div>
  <div class="lh-footer-left">
    <strong>DANIEL R. HALDEN, ESQ.</strong>
    Licensed in NC and FL<br>
    Board Certified in Civil Trial Law<br>
    by NTLB
  </div>
  <div class="lh-footer-right">
    2280 Birchwood Lane, Suite 410<br>
    Raleigh, NC 27609
    <span class="gap"></span>
    <b>T:</b> 919.555.0142<br>
    <b>F:</b> 919.555.0163<br>
    www.haldenlawpa.com
  </div>
</section>

<section class="sheet card-front">
  <div class="brand">
    <span class="brand-mark"></span>
    <span class="brand-name">HALDEN LAW</span>
  </div>
  <div class="card-contact">
    <div class="name">DANIEL R. HALDEN, ESQ.</div>
    <div class="lic">Licensed in NC and FL.</div>
    2280 Birchwood Lane, Suite 410<br>
    Raleigh, NC 27609<br>
    <span class="gap"></span>
    <b>Tel:</b> 919.555.0142<br>
    <b>Cell:</b> 919.555.0187<br>
    <b>Fax:</b> 919.555.0163<br>
    www.haldenlawpa.com<br>
    dan@haldenlawpa.com
  </div>
</section>

<section class="sheet card-back">
  <span class="brand-mark"></span>
  <p class="site">www.haldenlawpa.com</p>
</section>

<section class="sheet envelope-back">
  <svg class="flap" viewBox="0 0 531 76" aria-hidden="true">
    <path d="M0 0 H531 L524 18 Q515 58 480 73 Q470 76 455 76 H76 Q61 76 51 73 Q16 58 7 18 Z" fill="#f6f6f6" stroke="#dedede" stroke-width="1"/>
  </svg>
  <span class="brand-mark"></span>
</section>

<section class="sheet envelope-front">
  <div class="brand">
    <span class="brand-mark"></span>
    <span class="brand-name">HALDEN LAW</span>
    <p class="address">2280 Birchwood Lane,<br>Suite 410, Raleigh, NC 27609</p>
  </div>
</section>

</body>
</html>
```